Velorin Banner Design

We need banners for new company Velorin Holdings Limited located in Hong Kong. Velorin is an global online business platform, needs clean white, blue and red color mix banners.

Reason: I am extending for final design

Target Market(s)

Velorin an online Business Company have a target home based business owners and DIY website seekers.

Industry/Entity Type

Business

Colors
0355a3
ec2027
ffffff

Requirements
Must have
• Free Sign Up Button and Velorin Logo

```html
<!DOCTYPE html>
<html lang="en">
<head>
<meta charset="utf-8">
<title>Velorin Banner Set</title>
<link rel="stylesheet" href="https://fonts.googleapis.com/css2?family=Roboto+Condensed:wght@400;700&display=swap">
<style>
  :root {
    --blue: #0355a3;
    --red: #ec2027;
    --dark-red: #9b1c1f;
    --white: #ffffff;
    --yellow: #f9c31a;
    --slate: #4a4a4a;
    --slate-light: #6a6a6a;
    --logo-grey: #7d7d7d;
    --stage: #e9e9e9;
    --ink: #1a1a1a;
  }
  * { margin: 0; padding: 0; box-sizing: border-box; }
  html, body { width: 1200px; height: 588px; overflow: hidden; }
  body {
    background: var(--stage);
    font-family: "Roboto Condensed", "Arial Narrow", sans-serif;
    position: relative;
  }
  .banner { position: absolute; overflow: hidden; }
  .abs { position: absolute; }
  .brand {
    position: absolute; display: flex; align-items: center; gap: 6px;
    font-weight: 700; color: var(--logo-grey); letter-spacing: 1px;
  }
  .brand .dot { width: 0.55em; height: 0.55em; border-radius: 50%; background: var(--blue); }
  .btn {
    position: absolute; display: flex; align-items: center; justify-content: center;
    color: var(--white); background: var(--red); font-weight: 400; text-transform: uppercase;
  }

  /* Square banner */
  .square { left: 46px; top: 45px; width: 352px; height: 352px; background: var(--white); }
  .square .brand { left: 0; right: 0; top: 18px; justify-content: center; font-size: 36px; }
  .square .red-field { left: 0; top: 0; width: 352px; height: 352px; }
  .square .offer {
    left: 39px; top: 96px; width: 267px; height: 186px; background: var(--dark-red);
    border-radius: 6px; color: var(--white); text-align: center; padding-top: 12px;
    font-weight: 700; line-height: 1.15;
  }
  .square .offer .lead { font-size: 23px; text-shadow: 1px 1px 2px rgba(0,0,0,.4); }
  .square .offer .sub { font-size: 19px; margin-top: 2px; }
  .square .offer .divider { font-size: 18px; letter-spacing: 2px; margin: 6px 0 8px; font-weight: 400; }
  .square .offer .program { font-size: 18px; text-transform: uppercase; }
  .square .signup {
    left: 84px; top: 310px; width: 190px; height: 42px; background: var(--yellow);
    clip-path: polygon(8% 0, 100% 0, 100% 100%, 0 100%);
    display: flex; align-items: center; justify-content: center; gap: 10px;
    font-size: 17px; color: var(--ink);
  }
  .square .signup .arrow { width: 0; height: 0; border-left: 8px solid var(--ink);
    border-top: 6px solid transparent; border-bottom: 6px solid transparent; }

  /* Medium rectangle */
  .rect { left: 411px; top: 152px; width: 294px; height: 245px; background: var(--white); }
  .rect .slate-field { left: 0; top: 0; width: 294px; height: 175px; }
  .rect .tag {
    left: 6px; top: 30px; width: 198px; height: 44px; background: var(--white);
    display: flex; align-items: center; padding-left: 8px; font-size: 17px; color: var(--ink);
  }
  .rect .price { left: 212px; top: 24px; color: var(--white); font-size: 40px; line-height: 1; }
  .rect .per { left: 234px; top: 64px; color: var(--white); font-size: 11px; font-weight: 700; }
  .rect .program {
    left: 6px; top: 84px; width: 248px; height: 59px; background: var(--white);
    padding: 6px 8px; font-size: 19px; line-height: 1.05; color: var(--ink); text-transform: uppercase;
  }
  .rect .btn { left: 56px; top: 182px; width: 182px; height: 48px; font-size: 18px; }
  .rect .underline { left: 56px; top: 234px; width: 182px; height: 5px; background: var(--red); opacity: .6; }

  /* Small rectangle */
  .mini { left: 718px; top: 270px; width: 168px; height: 127px; background: var(--blue); }
  .mini .cap { left: 0; top: 0; width: 168px; height: 28px; background: var(--white); }
  .mini .brand { left: 0; right: 0; top: 3px; justify-content: center; font-size: 19px; gap: 4px; }
  .mini .lead { left: 0; right: 0; top: 32px; text-align: center; color: var(--white); font-size: 14px; font-weight: 700; }
  .mini .price { left: 26px; top: 48px; color: var(--white); font-weight: 700; font-size: 44px; line-height: 1; }
  .mini .per { left: 108px; top: 76px; color: var(--white); font-size: 13px; font-weight: 700; }
  .mini .btn { left: 38px; top: 101px; width: 89px; height: 24px; font-size: 11px; font-weight: 700; }

  /* Leaderboard */
  .board { left: 46px; top: 431px; width: 659px; height: 84px; background: var(--blue); }
  .board .offer {
    left: 6px; top: 11px; width: 229px; height: 60px; background: var(--white);
    color: var(--blue); font-weight: 700; padding: 5px 8px; line-height: 1.1;
  }
  .board .offer .l1 { font-size: 18px; }
  .board .offer .l2 { font-size: 21px; }
  .board .program { left: 246px; top: 13px; color: var(--white); font-weight: 700; font-size: 18px; text-transform: uppercase; }
  .board .btn { left: 284px; top: 48px; width: 144px; height: 31px; font-size: 14px; }
  .board .swoosh { left: 0; top: 0; width: 659px; height: 84px; }
  .board .brand { left: 544px; top: 56px; font-size: 21px; gap: 4px; }
</style>
</head>
<body>

  <section class="banner square" aria-label="Square banner">
    <svg class="abs red-field" viewBox="0 0 352 352" aria-hidden="true">
      <path d="M0 70 Q176 45 352 70 L352 352 L0 352 Z" fill="var(--red)"/>
    </svg>
    <div class="brand">VELORIN<span class="dot"></span></div>
    <div class="abs offer">
      <p class="lead">Create your own ecommerce<br>website @ $10/month</p>
      <p class="sub">&amp; start earning at the same time!</p>
      <p class="divider">-------------------------</p>
      <p class="program">Revolutionary single line<br>affiliate program</p>
    </div>
    <div class="abs signup">Free Sign Up <span class="arrow"></span></div>
  </section>

  <section class="banner rect" aria-label="Medium rectangle banner">
    <svg class="abs slate-field" viewBox="0 0 294 175" aria-hidden="true">
      <defs>
        <radialGradient id="slateGlow" cx="50%" cy="40%" r="70%">
          <stop offset="0" stop-color="var(--slate-light)"/>
          <stop offset="1" stop-color="var(--slate)"/>
        </radialGradient>
      </defs>
      <path d="M0 0 H294 V160 Q147 182 0 160 Z" fill="url(#slateGlow)"/>
    </svg>
    <div class="abs tag">ECOMMERCE WEBSITE @</div>
    <div class="abs price">$10</div>
    <div class="abs per">MONTH</div>
    <div class="abs program">Revolutionary single<br>line affiliate program</div>
    <div class="btn">Free Sign-Up</div>
    <div class="abs underline"></div>
  </section>

  <section class="banner mini" aria-label="Small rectangle banner">
    <div class="abs cap"></div>
    <div class="brand">VELORIN<span class="dot"></span></div>
    <p class="abs lead">ecommerce website at</p>
    <p class="abs price">$10/</p>
    <p class="abs per">month</p>
    <div class="btn">Free Sign-Up</div>
  </section>

  <section class="banner board" aria-label="Leaderboard banner">
    <svg class="abs swoosh" viewBox="0 0 659 84" aria-hidden="true">
      <path d="M520 84 Q580 40 659 38 L659 84 Z" fill="var(--white)"/>
    </svg>
    <div class="abs offer">
      <p class="l1">Create your own ecommerce</p>
      <p class="l2">website @ $10/month</p>
    </div>
    <p class="abs program">Revolutionary single line affiliate program</p>
    <div class="btn">Free Sign-Up</div>
    <div class="brand">VELORIN<span class="dot"></span></div>
  </section>

</body>
</html>
```